Safety training business card design

We need a buisness card design and logo for a small buisness that provides safety training through out the mining and civil construction industries. We provide first aid , confined space working at heights , machinery tickets, chainsaw, four wheel drive and four wheel motorbike training. We would like to use the design colors of navy blue, Fluro or lime green and white .

Industry/Entity Type

Construction

Contact Information for Business Card

Rillford Groundworks & Training , Neville Ormsby, rillford.skills@mailbox-example.net, ph 0481065374 abn 47 806 315 914

```html
<!DOCTYPE html>
<html lang="en">
<head>
<meta charset="utf-8">
<title>Rillford Groundworks &amp; Training – Business Card</title>
<link href="https://fonts.googleapis.com/css2?family=Tinos:wght@400&display=swap" rel="stylesheet">
<style>
  :root {
    --lime: #7ac143;
    --lime-deep: #6ab536;
    --lime-faint: #e3efd6;
    --white: #ffffff;
    --backdrop: #eeeeea;
    --card-shadow: rgba(0, 0, 0, 0.18);
  }
  * { box-sizing: border-box; margin: 0; padding: 0; }
  html, body {
    width: 1200px;
    height: 1000px;
    overflow: hidden;
    background: var(--backdrop);
    font-family: "Tinos", "Times New Roman", serif;
  }
  .canvas {
    position: relative;
    width: 1200px;
    height: 1000px;
  }
  .card {
    position: absolute;
    left: 270px;
    width: 660px;
    height: 378px;
    border-radius: 18px;
    overflow: hidden;
    box-shadow: 0 6px 18px var(--card-shadow);
  }
  /* Front side */
  .card-front {
    top: 60px;
    background: var(--lime);
    color: var(--white);
    display: flex;
    flex-direction: column;
    align-items: center;
    justify-content: center;
    gap: 34px;
  }
  .brand-mark {
    width: 150px;
    height: 150px;
    border-radius: 50%;
    border: 10px solid var(--white);
  }
  .brand-name {
    font-size: 30px;
    letter-spacing: 0.3px;
  }
  /* Back side */
  .card-back {
    top: 540px;
    background: var(--white);
  }
  .back-watermark {
    position: absolute;
    left: 175px;
    top: 20px;
    width: 340px;
    height: 340px;
    border-radius: 50%;
    border: 42px solid var(--lime-faint);
  }
  .back-heading {
    position: absolute;
    top: 52px;
    width: 100%;
    text-align: center;
    color: var(--lime);
    font-size: 29px;
    line-height: 1.15;
  }
  .contact-band {
    position: absolute;
    top: 178px;
    left: 0;
    width: 100%;
    height: 126px;
    background: var(--lime-deep);
    opacity: 0.94;
    color: var(--white);
    font-size: 26px;
  }
  .contact-item {
    position: absolute;
    display: flex;
    align-items: center;
    gap: 10px;
  }
  .contact-abn { left: 62px; top: 26px; }
  .contact-phone { right: 40px; top: 22px; }
  .contact-email { left: 110px; top: 74px; font-size: 24px; }
  .abn-badge {
    display: inline-flex;
    align-items: center;
    justify-content: center;
    width: 34px;
    height: 24px;
    border: 1.5px solid var(--white);
    border-radius: 6px;
    font-size: 10px;
  }
  .contact-icon { width: 26px; height: 26px; }
</style>
</head>
<body>
<main class="canvas">
  <section class="card card-front">
    <div class="brand-mark"></div>
    <p class="brand-name">Rillford Groundworks &amp; Training</p>
  </section>

  <section class="card card-back">
    <div class="back-watermark"></div>
    <h1 class="back-heading">Rillford Groundworks &amp; Training<br>Neville Ormsby</h1>
    <div class="contact-band">
      <p class="contact-item contact-abn"><span class="abn-badge">ABN</span>47 806 315 914</p>
      <p class="contact-item contact-phone">
        <svg class="contact-icon" viewBox="0 0 24 24" aria-hidden="true">
          <path fill="#ffffff" d="M7 2.5c.8-.4 1.6 0 2 .8l1.5 3.2c.3.7.1 1.5-.5 1.9l-1.3.9c.8 2.6 2.4 5.3 4.4 7l1.3-.8c.6-.4 1.4-.3 1.9.3l2.2 2.8c.5.7.4 1.6-.3 2.1-1.5 1.1-3.4 1.5-5 .5C8.6 18.6 5.2 12.6 5 7.4c-.1-2 .6-4 2-4.9z"/>
        </svg>048 106 5374</p>
      <p class="contact-item contact-email">
        <svg class="contact-icon" viewBox="0 0 28 20" aria-hidden="true" style="width:30px;height:22px">
          <rect x="1" y="1" width="26" height="18" fill="none" stroke="#ffffff" stroke-width="1.6"/>
          <path d="M1 1l13 10L27 1" fill="none" stroke="#ffffff" stroke-width="1.6"/>
        </svg>rillford.skills@mailbox-example.net</p>
    </div>
  </section>
</main>
</body>
</html>
```